Velmora Water Purification

We need a website set up on a "Free account" WordPress platform. (This is the type of Wordpress site that you can sign up for and create online for free (not a server-hosted type.)
The website will be for a water purification company. They install devices in homes to purify the water for safer drinking, bathing, and cleaning.
Our logo is attached. Please keep color scheme of the website consistent with the logo.
Water Purification

```html
<!DOCTYPE html>
<html lang="en">
<head>
<meta charset="utf-8">
<title>Velmora Water Purification</title>
<link href="https://fonts.googleapis.com/css2?family=Lato:wght@300;400;700;900&display=swap" rel="stylesheet">
<style>
  :root {
    --navy: #1f4160;
    --ink: #3b3f44;
    --text: #555a60;
    --header-bg: #f4f4f4;
    --rule: #8ea2b0;
    --card-border: #8a9aa5;
    --nav: #7aa3bd;
    --white: #ffffff;
    --hero-light: #b9cdd2;
    --hero-mid: #5f8791;
    --hero-dark: #1f3d4d;
  }
  * { margin: 0; padding: 0; box-sizing: border-box; }
  html, body { width: 1200px; height: 2195px; overflow: hidden; }
  body {
    position: relative;
    background: var(--white);
    font-family: "Lato", sans-serif;
    color: var(--text);
  }
  .abs { position: absolute; }

  /* Header */
  .site-header { left: 0; top: 0; width: 1200px; height: 173px; background: var(--header-bg); }
  .header-divider { left: 330px; top: 0; width: 3px; height: 582px; background: var(--white); z-index: 3; }
  .brand { left: 88px; top: 70px; width: 225px; display: flex; align-items: center; gap: 8px; white-space: nowrap; }
  .brand-dot { flex: none; width: 16px; height: 16px; border-radius: 50%; background: var(--navy); }
  .brand-name { font-size: 14px; font-weight: 700; color: var(--navy); }
  .main-nav { left: 852px; top: 76px; display: flex; gap: 14px; }
  .main-nav a {
    font-size: 10px; letter-spacing: 0.8px; color: var(--nav);
    text-decoration: none; text-transform: uppercase; padding-bottom: 9px;
  }
  .main-nav a.is-active { border-bottom: 1px solid var(--nav); }

  /* Hero */
  .hero-photo {
    left: 0; top: 173px; width: 1200px; height: 409px;
    background: radial-gradient(ellipse at 55% 35%, var(--hero-light), var(--hero-mid) 55%, var(--hero-dark));
  }
  .hero-notch { left: 162px; top: 559px; width: 168px; height: 23px; background: var(--white); }
  .hero-panel { left: 332px; top: 205px; width: 631px; height: 391px; border: 2px solid var(--white); z-index: 2; }
  .hero-panel-lower {
    position: absolute; left: 0; top: 197px; width: 100%; height: 178px;
    background: rgba(20, 48, 70, 0.55); border-top: 2px solid var(--white);
  }
  .hero-panel-base { position: absolute; left: 0; bottom: 0; width: 100%; height: 14px; background: #2c4c66; }
  .hero-title { position: absolute; top: 48px; width: 100%; text-align: center; color: #1e2a33; }
  .hero-title .line-1 { display: block; font-size: 40px; font-weight: 300; line-height: 50px; }
  .hero-title .line-2 { display: block; font-size: 52px; font-weight: 700; letter-spacing: 5px; color: var(--white); line-height: 54px; }
  .hero-lead {
    position: absolute; top: 248px; left: 60px; width: 507px; text-align: center;
    font-size: 20px; font-weight: 300; line-height: 28px; color: var(--white);
  }

  /* About */
  .rule { height: 1px; background: var(--rule); }
  .about-rule { left: 162px; top: 691px; width: 242px; }
  .section-title { font-size: 32px; font-weight: 300; color: var(--navy); }
  .section-title strong { font-weight: 700; }
  .about-title { left: 275px; top: 718px; }
  .about-text { left: 275px; top: 778px; width: 390px; font-size: 15px; font-weight: 700; line-height: 22.6px; color: #666b70; }
  .photo-glass { left: 151px; top: 890px; width: 249px; height: 339px; background: linear-gradient(180deg, #f4f2ec, #e9d9a6 60%, #c99b3b 80%, #f2f2f2); }
  .photo-warehouse-top { left: 704px; top: 758px; width: 227px; height: 228px; background: linear-gradient(160deg, #9fc4dc, #3d6f97 60%, #2a4f72); }
  .photo-warehouse-bottom { left: 541px; top: 986px; width: 390px; height: 160px; background: linear-gradient(180deg, #5f8cad, #3f6f93 55%, #8fb0c6); }
  .about-aside { left: 704px; top: 1246px; width: 390px; font-size: 14.5px; line-height: 22px; color: var(--ink); }
  .products-rule { left: 546px; top: 1405px; width: 654px; }

  /* Products */
  .products-title { left: 146px; top: 1474px; }
  .product-card { background: var(--white); border: 1px solid var(--card-border); }
  .product-card .photo { position: absolute; background: linear-gradient(180deg, #cfcfcf, #f3f3f3 55%, #e2e2e2); }
  .product-card .device {
    position: absolute; left: 50%; transform: translateX(-50%);
    background: var(--white); border-radius: 3px; box-shadow: 0 1px 3px rgba(0,0,0,0.15);
  }
  .product-name { position: absolute; font-weight: 900; color: var(--navy); letter-spacing: 1.5px; }
  .product-text { position: absolute; color: var(--ink); }

  .card-side { top: 1578px; width: 284px; height: 282px; }
  .card-side .photo { left: 15px; top: 20px; width: 254px; height: 140px; }
  .card-side .device { top: 36px; width: 140px; height: 76px; }
  .card-side .product-name { left: 22px; top: 159px; font-size: 23px; }
  .card-side .product-text { left: 22px; top: 195px; width: 230px; font-size: 11.5px; line-height: 17px; }
  .card-left { left: 142px; }
  .card-right { left: 789px; }

  .card-main { left: 389px; top: 1640px; width: 436px; height: 415px; z-index: 2; }
  .card-main .photo { left: 36px; top: 41px; width: 363px; height: 201px; }
  .card-main .device { top: 50px; width: 260px; height: 110px; }
  .card-main .product-name { left: 50px; top: 224px; font-size: 32px; letter-spacing: 2px; }
  .card-main .product-text { left: 50px; top: 283px; width: 330px; font-size: 15px; font-weight: 700; line-height: 23px; color: #666b70; }
</style>
</head>
<body>
  <header class="abs site-header"></header>
  <div class="abs brand">
    <span class="brand-dot"></span>
    <span class="brand-name">Velmora Water Purification</span>
  </div>
  <nav class="abs main-nav">
    <a href="#" class="is-active">Home</a>
    <a href="#">About us</a>
    <a href="#">Products</a>
    <a href="#">Contact</a>
  </nav>

  <section class="hero">
    <div class="abs hero-photo" role="img" aria-label="Close-up of water droplets on soft teal fibres"></div>
    <div class="abs hero-notch"></div>
    <div class="abs header-divider"></div>
    <div class="abs hero-panel">
      <h1 class="hero-title">
        <span class="line-1">Safe drinking water</span>
        <span class="line-2">EVERYWHERE</span>
      </h1>
      <div class="hero-panel-lower"></div>
      <p class="hero-lead">Lorem ipsum dolor sit amet enim. Etiam ullamcorper. Suspendisse a pellentesque dui, non felis. Maecenas malesuada elit lectus felis, malesuada ultricies.</p>
      <div class="hero-panel-base"></div>
    </div>
  </section>

  <section class="about">
    <div class="abs rule about-rule"></div>
    <h2 class="abs section-title about-title">About <strong>us</strong></h2>
    <p class="abs about-text">Lorem ipsum dolor sit amet enim. Etiam ullamcorper. Suspendisse a pellentesque dui, non felis. Maecenas malesuada elit lectus felis, malesuada ultricies. Curabitur et ligula. Ut molestie a, ultricies porta urna. Vestibulum commodo volutpat a, convallis ac, laoreet enim.</p>
    <div class="abs photo-glass" role="img" aria-label="Glass of water with a lemon slice splashing"></div>
    <div class="abs photo-warehouse-top" role="img" aria-label="Warehouse ceiling with steel beams and lights"></div>
    <div class="abs photo-warehouse-bottom" role="img" aria-label="Warehouse loading dock with a truck"></div>
    <p class="abs about-aside">Lorem ipsum dolor sit amet enim. Etiam ullamcorper. Suspendisse a pellentesque dui, non felis. Maecenas malesuada elit lectus felis.</p>
    <div class="abs rule products-rule"></div>
  </section>

  <section class="products">
    <h2 class="abs section-title products-title">Our Products</h2>

    <article class="abs product-card card-side card-left">
      <div class="photo" role="img" aria-label="White water purifier unit on a table"><div class="device"></div></div>
      <h3 class="product-name">MODEL 2</h3>
      <p class="product-text">Lorem ipsum dolor sit amet enim. Etiam ullamcorper. Suspendisse a pellentesque</p>
    </article>

    <article class="abs product-card card-side card-right">
      <div class="photo" role="img" aria-label="White water purifier unit on a table"><div class="device"></div></div>
      <h3 class="product-name">MODEL 2</h3>
      <p class="product-text">Lorem ipsum dolor sit amet enim. Etiam ullamcorper. Suspendisse a pellentesque dui</p>
    </article>

    <article class="abs product-card card-main">
      <div class="photo" role="img" aria-label="White water purifier unit on a table"><div class="device"></div></div>
      <h3 class="product-name">MODEL 1</h3>
      <p class="product-text">Lorem ipsum dolor sit amet enim. Etiam ullamcorper. Suspendisse a pellentesque dui</p>
    </article>
  </section>
</body>
</html>
```